I am seeking a label design for a new product to be launched at my salon, Velmora Salon. However, for the products, I am solely utilizing the branding "Velmora."
I am interested in exploring various bathroom modern clean concepts for the labels on our shampoo and conditioner ROUND white 10 Oz bottles.
I need a shampoo label design that will attract many customers with its appeal. As the owner of a hair salon, I aim to create something unique and exquisite, with a clean and sleek, high-class, and elegant print for the shampoo. I am open to suggestions and eager to see different designs that may better suit my vision.

Also if you could apply the label on the bottle, would be amazing.

Target Market(s)

Anyone seeking healthy, smooth, fast-growing, and beautiful hair is our target market—primarily women, though we welcome all clients.

Industry/Entity Type

Hair and Spa.

Colors

Designer to choose colors to be used in the design.

Requirements
Must have
• Clean look, and no overcrowded with elements, No bright or solid dark colors .
Nice to have
• Please refer to the attached references below, but I am open to suggestions as well.

```html
<!DOCTYPE html>
<html lang="en">
<head>
<meta charset="utf-8">
<title>Velmora Revitalizing Shampoo Label</title>
<link rel="stylesheet" href="https://fonts.googleapis.com/css2?family=Questrial&family=Roboto:wght@300&family=Cormorant+Garamond:wght@500&display=swap">
<style>
  :root {
    --backdrop: #7ca39d;
    --label-white: #ffffff;
    --plaque-top: #5d8d86;
    --plaque-bottom: #4e7e77;
    --ink-light: #eef4f2;
    --leaf-deep: #3f7a5c;
    --leaf-mid: #8db9a4;
    --bloom-mint: #d6ece3;
  }
  * { margin: 0; padding: 0; box-sizing: border-box; }
  html, body {
    width: 1200px;
    height: 1159px;
    overflow: hidden;
    background: var(--backdrop);
  }
  .canvas {
    position: relative;
    width: 1200px;
    height: 1159px;
  }
  .label {
    position: absolute;
    left: 320px;
    top: 60px;
    width: 560px;
    height: 1040px;
    background: var(--label-white);
    border-radius: 14px;
    overflow: hidden;
  }
  .floral-artwork {
    position: absolute;
    inset: 12px;
    border-radius: 10px;
    background:
      radial-gradient(ellipse at 25% 12%, var(--bloom-mint) 0%, transparent 38%),
      radial-gradient(ellipse at 80% 18%, var(--leaf-deep) 0%, transparent 30%),
      radial-gradient(ellipse at 35% 90%, var(--bloom-mint) 0%, transparent 35%),
      radial-gradient(ellipse at 75% 88%, var(--leaf-deep) 0%, transparent 32%),
      linear-gradient(180deg, var(--leaf-mid) 0%, var(--bloom-mint) 50%, var(--leaf-mid) 100%);
    opacity: 0.85;
  }
  .plaque {
    position: absolute;
    left: 85px;
    top: 300px;
    width: 390px;
    height: 510px;
  }
  .plaque-frame {
    position: absolute;
    left: 0;
    top: 0;
  }
  .plaque-content {
    position: absolute;
    inset: 0;
    color: var(--ink-light);
    text-align: center;
  }
  .brand-mark {
    position: absolute;
    top: 78px;
    left: 0;
    right: 0;
    display: flex;
    align-items: center;
    justify-content: center;
    gap: 12px;
    font-family: "Questrial", sans-serif;
    font-size: 30px;
    letter-spacing: 2px;
  }
  .brand-dot {
    width: 12px;
    height: 12px;
    border-radius: 50%;
    background: var(--ink-light);
  }
  .product-variant {
    position: absolute;
    top: 226px;
    left: 0;
    right: 0;
    font-family: "Roboto", sans-serif;
    font-weight: 300;
    font-size: 20px;
  }
  .product-name {
    position: absolute;
    top: 256px;
    left: 0;
    right: 0;
    font-family: "Questrial", sans-serif;
    font-weight: 400;
    font-size: 46px;
    letter-spacing: 1px;
  }
  .divider {
    position: absolute;
    top: 322px;
    left: 145px;
  }
  .net-volume {
    position: absolute;
    top: 430px;
    left: 0;
    right: 0;
    font-family: "Cormorant Garamond", serif;
    font-weight: 500;
    font-size: 22px;
    letter-spacing: 1px;
    font-variant-numeric: lining-nums;
  }
</style>
</head>
<body>
<main class="canvas">
  <section class="label">
    <div class="floral-artwork" role="img" aria-label="Watercolour mint roses with eucalyptus and green leaves framing the label"></div>
    <div class="plaque">
      <svg class="plaque-frame" width="390" height="510" viewBox="0 0 390 510" aria-hidden="true">
        <defs>
          <linearGradient id="plaqueFill" x1="0" y1="0" x2="0" y2="1">
            <stop offset="0" stop-color="#5d8d86"/>
            <stop offset="1" stop-color="#4e7e77"/>
          </linearGradient>
        </defs>
        <path d="M0 72 L22 72 L22 52 Q62 52 104 36 Q195 0 286 36 Q328 52 368 52 L368 72 L390 72 L390 510 L0 510 Z" fill="url(#plaqueFill)"/>
        <path d="M12 82 L32 82 L32 62 Q70 62 108 48 Q195 16 282 48 Q320 62 358 62 L358 82 L378 82 L378 498 L12 498 Z" fill="none" stroke="#eef4f2" stroke-width="1.5"/>
      </svg>
      <div class="plaque-content">
        <div class="brand-mark"><span class="brand-dot"></span><span>Velmora</span></div>
        <p class="product-variant">Revitalizing</p>
        <h1 class="product-name">SHAMPOO</h1>
        <svg class="divider" width="100" height="30" viewBox="0 0 100 30" aria-hidden="true">
          <path d="M2 4 Q2 12 12 12 L42 12 L50 24 L58 12 L88 12 Q98 12 98 4" fill="none" stroke="#eef4f2" stroke-width="1.5"/>
        </svg>
        <p class="net-volume">10 OZ</p>
      </div>
    </div>
  </section>
</main>
</body>
</html>
```